Let's help people Kestrel with better hearing!

I need a business card for my private practice. I am a Dr. of Audiology and focus on hearing and tinnitus (ringing in the ears) treatment. My practice is named "Kestrel Hearing and Tinnitus Solutions". I want to communicate the idea of improved quality of life utilizing a natural color pallet Love the color turquoise as an accent. Want a professional look, while eye catching. I'm open to nontraditional design aesthetic. Something to get excited about and motivate people to improve their lives!

```html
<!DOCTYPE html>
<html lang="en">
<head>
<meta charset="utf-8">
<title>Kestrel Hearing and Tinnitus Solutions – Business Card</title>
<link rel="stylesheet" href="https://fonts.googleapis.com/css2?family=Didact+Gothic&display=swap">
<style>
  :root {
    --backdrop: #ecedee;
    --card-mint: #d3e7d9;
    --teal: #22b2a6;
    --teal-soft: rgba(34, 178, 166, 0.55);
    --teal-faint: rgba(34, 178, 166, 0.12);
    --panel-white: #ffffff;
    --card-shadow: rgba(40, 60, 60, 0.18);
  }

  * { box-sizing: border-box; margin: 0; padding: 0; }

  html, body {
    width: 1200px;
    height: 900px;
    overflow: hidden;
    background: var(--backdrop);
    font-family: "Didact Gothic", "Century Gothic", sans-serif;
    color: var(--teal);
  }

  .canvas {
    position: relative;
    width: 1200px;
    height: 900px;
  }

  .card {
    position: absolute;
    width: 630px;
    height: 360px;
    background: var(--card-mint);
    box-shadow: 0 10px 26px var(--card-shadow);
    overflow: hidden;
  }

  .card--back  { left: 470px; top: 60px; }
  .card--front { left: 100px; top: 480px; }

  .wave-band {
    position: absolute;
    left: 0;
    right: 0;
    top: 50%;
    height: 46%;
    transform: translateY(-50%);
    background: linear-gradient(180deg,
      rgba(211, 231, 217, 0) 0%,
      var(--teal-faint) 30%,
      rgba(34, 178, 166, 0.2) 50%,
      var(--teal-faint) 70%,
      rgba(211, 231, 217, 0) 100%);
  }

  .panel {
    position: absolute;
    left: 50%;
    top: 50%;
    transform: translate(-50%, -50%);
    background: var(--panel-white);
    box-shadow: 0 0 14px 4px var(--teal-soft);
    text-align: center;
  }

  /* Front side */
  .card--front .panel {
    width: 300px;
    height: 196px;
    display: flex;
    flex-direction: column;
    justify-content: center;
    align-items: center;
    gap: 6px;
  }

  .practice-name {
    font-size: 52px;
    line-height: 1;
    letter-spacing: 1px;
  }

  .practice-tagline {
    font-size: 20px;
    line-height: 1.2;
    letter-spacing: 0.5px;
    text-transform: uppercase;
  }

  /* Back side */
  .card--back .panel {
    width: 248px;
    height: 144px;
    padding-top: 10px;
    line-height: 1.12;
  }

  .contact__name {
    font-size: 15px;
    font-weight: 700;
    letter-spacing: 0.4px;
  }

  .contact__credentials,
  .contact__title {
    font-size: 14px;
    letter-spacing: 0.4px;
  }

  .contact__phone {
    font-size: 13px;
    font-weight: 700;
    letter-spacing: 0.6px;
    margin-top: 2px;
  }

  .contact__online {
    font-size: 12px;
    letter-spacing: 0.4px;
  }

  .contact__address {
    font-size: 10.5px;
    letter-spacing: 0.4px;
    margin-top: 2px;
  }
</style>
</head>
<body>
  <main class="canvas">

    <section class="card card--back" aria-label="Business card back">
      <div class="wave-band" role="img" aria-label="Dotted turquoise sound-wave pattern running across the card"></div>
      <div class="panel contact">
        <p class="contact__name">Marin Ellsworth</p>
        <p class="contact__credentials">AuD, CCC-A</p>
        <p class="contact__title">Doctor of Audiology</p>
        <p class="contact__phone">(555) 014-2286</p>
        <p class="contact__online">hearhealthkestrel@mailbox.com</p>
        <p class="contact__online">www.hearhealthkestrel.com</p>
        <p class="contact__address">2740 Hwy 18</p>
        <p class="contact__address">Suite 300</p>
        <p class="contact__address">Alder Falls, TN 38190</p>
      </div>
    </section>

    <section class="card card--front" aria-label="Business card front">
      <div class="wave-band" role="img" aria-label="Dotted turquoise sound-wave pattern running across the card"></div>
      <div class="panel brand">
        <p class="practice-name">Kestrel</p>
        <p class="practice-tagline">Hearing &amp; Tinnitus<br>Solutions</p>
      </div>
    </section>

  </main>
</body>
</html>
```